BrallonGrip Screw Box and Carton Design

We are BrallonGrip, a new screw and nail supplier from Ireland. We need box designs branded for our new launch of screws and nails, Outer carton and inner individual boxes. We would like our branding to portray the image of a professional company. We have our logo attached which we would like to stand out so that people recognise the box if it were to be seen from a distance or in a shop.

Target Market(s)

Construction Industry

Industry/Entity Type

Construction

Contact Information for Business Card

Cathal Dunmore
Owner
07481236094
cathal@brallongrip.co.uk

Font styles to use
Sans Serif

Colors
3277b5

Requirements
Must have
• The Carton should be cost effective for the box maker. The carton will contain 10 boxes. If you could design them in such a way that they can be manipulated easily to cater for the various sizes. The internal boxes that hold the screws will have colour. I like the layout of the Kestrove box where the lid folds out over the front of the box. Blue colour #009ee2 Grey colour #4a4a49
Nice to have
• I would like some upgraded design to the original BrallonGrip box in the picture. I feel that this design does not cater well for labels or information to be placed on the box.

```html
<!DOCTYPE html>
<html lang="en">
<head>
<meta charset="utf-8">
<title>BrallonGrip – Screw Box Lid Panel</title>
<link rel="stylesheet" href="https://fonts.googleapis.com/css2?family=Montserrat:wght@800&display=swap">
<style>
  :root {
    --stage-light: #d9d9d9;
    --stage-dark: #7c7c7e;
    --box-body: #333333;
    --brand-blue: #009ee2;
    --brand-grey: #4a4a49;
  }
  html, body {
    margin: 0;
    padding: 0;
    width: 1200px;
    height: 890px;
    overflow: hidden;
  }
  .canvas {
    position: relative;
    width: 1200px;
    height: 890px;
    background: radial-gradient(ellipse at 50% 48%, var(--stage-light) 0%, #b4b4b5 45%, var(--stage-dark) 100%);
  }
  .box-panel {
    position: absolute;
    inset: 0;
    width: 1200px;
    height: 890px;
  }
  .panel-body { fill: var(--box-body); }
  .stripe-blue { fill: var(--brand-blue); }
  .stripe-grey { fill: var(--brand-grey); }
  .brand-name {
    font-family: "Montserrat", Arial, sans-serif;
    font-weight: 800;
    font-size: 66px;
    fill: var(--brand-blue);
  }
</style>
</head>
<body>
<main class="canvas">
  <svg class="box-panel" viewBox="0 0 1200 890" xmlns="http://www.w3.org/2000/svg">
    <polygon class="panel-body"
      points="355,172 832,167 850,180 995,405 1025,410 940,690 258,716 158,418 205,413"/>

    <!-- upper left flap -->
    <polygon class="stripe-blue" points="372,172 388,172 212,415 199,415"/>
    <polygon class="stripe-grey" points="398,172 413,172 236,415 222,415"/>
    <!-- lower left flap -->
    <polygon class="stripe-blue" points="188,420 199,420 289,714 278,714"/>
    <polygon class="stripe-grey" points="212,420 228,420 312,714 296,714"/>
    <!-- upper right flap -->
    <polygon class="stripe-blue" points="812,168 826,168 994,410 980,410"/>
    <polygon class="stripe-grey" points="786,168 800,168 972,410 958,410"/>
    <!-- lower right flap -->
    <polygon class="stripe-blue" points="983,412 996,412 910,692 898,692"/>
    <polygon class="stripe-grey" points="957,412 972,412 890,692 876,692"/>

    <text class="brand-name" x="590" y="541" text-anchor="middle">BrallonGrip</text>
  </svg>
</main>
</body>
</html>
```